Modern, Clean website for painting service.

We are working with a company called Brushwell Crafts and building a new website for them.

Some sites to use for content/competitors and inspiration:

https://www.coatvantaged.com
https://ridgeline-hue.com
https://tedvarnokcoating.com

Thank you for taking the time to consider designing a website for us. We are web developers based in Stockton, CA, USA. Most of our projects go through the same process. Understanding this process may help you win a project with us. We custom-code all of our websites in-house. We don’t have any requirements as to what tools you use for your design, but we prefer Figma files. For any design that we label as four-stars, we send it to the client for review. The client picks the final design they want us to use. Once we complete this process, we will continue to show additional clients all the four-star sites and purchase them later. Your designs will have multiple chances to sell. For better chances of success, we ask that you follow these guidelines.

IMAGES:
If you use any images or icons in the design, we ask that you have a link to the asset so we can purchase the image/icon. Most of the designs we submit do not have the customer’s images on them unless they have some great images. Be creative; show us the feeling you are trying to portray with your image choices. Use any royalty-free site you choose. We subscribe to Kelvra and mainly use their images, but we can purchase images outside of Kelvra. PLEASE NOTE: we will not submit designs to clients with watermarks on the images.

FONTS:
We ask that you identify the fonts used in the design. This can be done in a message if you want. We typically use Google Fonts and Kelvra Type.

CONTENT:
We're always open to different content and ideas. We often submit designs with stock images so the client can see our vision. We typically take pictures after the website launch to use their images with our vision. Lorem Ipsum is fine for paragraphs, but we ask that you write the headers in correct English. We want to be able to show the vision and identify the sections of the website.

INSPIRATION:
We typically add a couple of links in the brief of websites we like to help you get started in your design.

REVISIONS:
We do not often ask for revisions of the designs unless we see something in the design that may not appeal to the client. If there are slight changes that we want to make, we do that in the development process.

FEEDBACK:
We rarely give feedback on designs during the design process. We are working on many website projects and do not have the time to provide feedback. We usually respond if your request is well thought out and asks specific questions, but a note asking “feedback, please” usually goes unanswered.

```html
<!DOCTYPE html>
<html lang="en">
<head>
<meta charset="utf-8">
<title>Brushwell Crafts — Painting Services</title>
<link rel="stylesheet" href="https://fonts.googleapis.com/css2?family=Lexend:wght@400;500;600;700&family=Poppins:wght@400;500;600&display=swap">
<style>
:root{
  --navy:#0f2147;
  --navy-deep:#0a1834;
  --red:#b4173a;
  --red-dark:#8e1029;
  --light:#f3f3f5;
  --white:#ffffff;
  --text:#333844;
  --muted:#6b7080;
}
*{box-sizing:border-box;margin:0;padding:0}
html,body{width:1200px;height:5104px;overflow:hidden}
body{font-family:"Poppins",sans-serif;color:var(--text);background:var(--white);position:relative}
h1,h2,h3,h4{font-family:"Lexend",sans-serif}
section,header,footer{position:absolute;left:0;width:1200px}
.abs{position:absolute}
.btn{position:absolute;display:flex;align-items:center;justify-content:center;border-radius:30px;font-family:"Poppins",sans-serif;font-weight:600;font-size:13px;letter-spacing:.5px;color:var(--white);text-decoration:none}
.btn-red{background:var(--red)}
.btn-navy{background:var(--navy)}
.btn-outline{border:2px solid var(--white)}
.section-title{position:absolute;left:0;width:1200px;text-align:center;font-size:52px;font-weight:500;color:var(--navy);letter-spacing:1px}
.title-rule{position:absolute;height:3px;width:70px;background:var(--red)}
.brand{display:flex;align-items:center;gap:10px;font-family:"Lexend",sans-serif;font-weight:600;font-size:24px;color:var(--navy)}
.brand-mark{width:22px;height:22px;background:var(--red)}

/* header */
.site-header{top:0;height:120px;background:var(--white);z-index:3}
.site-header .brand{position:absolute;left:80px;top:40px}
.main-nav{position:absolute;right:76px;top:50px;display:flex;gap:34px;font-size:15px;font-weight:500;color:var(--navy);text-transform:uppercase}
.main-nav .active{color:var(--red);position:relative}
.main-nav .active::after{content:"";position:absolute;left:0;right:0;bottom:-10px;height:2px;background:var(--red)}

/* hero */
.hero{top:120px;height:700px;overflow:hidden}
.hero-photo{position:absolute;left:540px;top:0;width:660px;height:700px;background:linear-gradient(135deg,#e9ecef 0%,#cfd4da 45%,#f6f6f6 70%,#a7adb5 100%)}
.hero-panel{position:absolute;left:0;top:0}
.hero h1{position:absolute;left:72px;top:250px;width:560px;font-size:47px;line-height:58px;font-weight:600;color:var(--white);text-transform:uppercase;white-space:nowrap}
.hero p{position:absolute;left:72px;top:402px;width:440px;font-size:15px;line-height:24px;color:var(--white);font-weight:500}

/* about */
.about{top:820px;height:640px}
.about-frame{position:absolute;left:88px;top:100px;width:396px;height:432px;border:4px solid var(--red)}
.about-photo{position:absolute;left:104px;top:116px;width:372px;height:400px;background:linear-gradient(160deg,#7fa6c9 0%,#b9c9d6 35%,#6d7d62 70%,#485a3e 100%)}
.about h2{position:absolute;left:556px;top:112px;font-size:52px;font-weight:500;color:var(--navy)}
.about .title-rule{left:556px;top:186px}
.about p{position:absolute;left:556px;top:226px;width:570px;font-size:13px;line-height:24px;color:var(--text)}

/* services */
.services{top:1460px;height:840px}
.services-band{position:absolute;left:0;top:0;width:1200px;height:440px;background:linear-gradient(120deg,var(--red-dark) 0%,var(--red) 55%,#c8344f 100%)}
.services .section-title{top:92px;color:var(--white)}
.services .title-rule{left:565px;top:168px;background:var(--white)}
.services .lead{position:absolute;left:150px;top:200px;width:900px;text-align:center;font-size:14px;line-height:24px;color:var(--white)}
.service-cards{position:absolute;left:76px;top:332px;display:flex;gap:16px}
.service-card{width:251px;height:308px;background:var(--navy)}
.service-card .photo{height:228px}
.service-card h3{height:80px;display:flex;align-items:center;justify-content:center;font-family:"Poppins",sans-serif;font-size:18px;font-weight:600;color:var(--white)}

/* why */
.why{top:2300px;height:600px;background:var(--light)}
.why .section-title{top:88px}
.why .title-rule{left:565px;top:164px}
.why .lead{position:absolute;left:150px;top:214px;width:900px;text-align:center;font-size:14px;line-height:24px}
.why-cards{position:absolute;left:180px;top:308px;display:flex;gap:16px}
.why-card{width:198px;height:204px;text-align:center;color:var(--white);padding-top:26px}
.why-card.navy{background:var(--navy)}
.why-card.red{background:var(--red)}
.why-card .icon{width:52px;height:52px;margin:0 auto 22px;border-radius:50%;display:flex;align-items:center;justify-content:center}
.why-card.navy .icon{background:var(--red)}
.why-card.red .icon{background:var(--navy)}
.why-card h4{font-family:"Poppins",sans-serif;font-size:14px;font-weight:600;margin-bottom:8px}
.why-card p{font-size:12px;line-height:18px;padding:0 18px}

/* cta */
.cta{top:2900px;height:390px;background:linear-gradient(100deg,var(--navy-deep) 0%,#243a66 45%,#3d5580 70%,#1a2c52 100%)}
.cta h2{position:absolute;left:0;top:124px;width:1200px;text-align:center;font-size:54px;line-height:68px;font-weight:500;color:var(--white)}
.cta .btn{left:500px;top:298px;width:200px;height:54px}

/* reviews */
.reviews{top:3290px;height:750px}
.reviews .section-title{top:90px}
.reviews .title-rule{left:565px;top:166px}
.review-box{position:absolute;padding:30px 24px 0 80px;font-size:13px;line-height:20px;color:var(--white);border-radius:10px}
.review-box .quote{position:absolute;left:36px;top:24px;font-family:"Lexend",sans-serif;font-size:48px;line-height:48px}
.review-red{left:264px;top:334px;width:320px;height:186px;background:var(--red)}
.review-navy{left:648px;top:416px;width:320px;height:194px;background:var(--navy)}
.avatar{position:absolute;width:64px;height:64px;border-radius:50%;background:linear-gradient(#d8d8dc,#9aa0aa);border:3px solid var(--white);box-shadow:0 0 0 1px #ddd}
.reviewer h4{font-family:"Poppins",sans-serif;font-size:15px;font-weight:600;color:var(--navy)}
.reviewer span{display:block;font-size:12px;color:var(--muted)}
.stars{color:#f2b01e;font-size:13px;letter-spacing:2px}
.arrow{position:absolute;width:44px;height:44px;border-radius:50%;display:flex;align-items:center;justify-content:center}

/* gallery */
.gallery{top:4040px;height:560px;background:var(--light)}
.gallery .section-title{top:82px}
.gallery .title-rule{left:565px;top:158px}
.gallery-row{position:absolute;left:140px;top:232px;display:flex;gap:10px}
.gallery-row div{width:222px;height:228px}

/* footer */
.site-footer{top:4600px;height:464px;background:var(--navy);color:var(--white)}
.site-footer .brand{position:absolute;left:100px;top:110px;color:var(--white)}
.socials{position:absolute;left:128px;top:206px;display:flex;gap:8px}
.socials span{width:24px;height:24px;background:var(--white);border-radius:3px}
.foot-col{position:absolute;top:74px}
.foot-col h4{font-size:17px;font-weight:500;margin-bottom:22px;text-transform:uppercase}
.foot-col li{list-style:none;font-size:14px;line-height:30px;display:flex;align-items:center;gap:10px}
.foot-col li::before{content:"";width:6px;height:6px;border-radius:50%;background:var(--red)}
.contact-item{display:flex;gap:12px;font-size:13px;line-height:20px;margin-bottom:16px}
.contact-item .ic{width:26px;height:26px;border-radius:50%;background:var(--red);flex:none}
.newsletter p{font-size:13px;line-height:20px;width:230px;margin-bottom:14px}
.newsletter .field{width:220px;height:36px;background:var(--white);border-radius:2px}
.newsletter .btn{position:static;width:110px;height:32px;border-radius:2px;margin-top:12px;font-size:12px}
.copyright{position:absolute;left:0;top:5064px;width:1200px;height:40px;background:var(--red);color:var(--white);font-size:13px;display:flex;align-items:center;justify-content:center}
</style>
</head>
<body>

<header class="site-header">
  <div class="brand"><span class="brand-mark"></span>Brushwell Crafts</div>
  <nav class="main-nav">
    <span class="active">Home</span><span>About Us</span><span>Services</span><span>Testimonials ▾</span><span>Gallery</span><span>Contact Us</span>
  </nav>
</header>

<section class="hero">
  <div class="hero-photo" role="img" aria-label="Bright modern interior with a white spiral staircase"></div>
  <svg class="hero-panel" width="600" height="700" viewBox="0 0 600 700">
    <polygon points="0,0 590,0 560,700 0,700" fill="#0f2147"/>
    <polygon points="560,0 590,0 560,700 540,700" fill="#b4173a"/>
  </svg>
  <h1>High Quality<br>Brushwell Crafts</h1>
  <p>Lorem ipsum dolor sit amet, consectetur adipiscing elit, sed do eiusmod tempor incididunt ut labore et dolore magna</p>
  <a class="btn btn-red" style="left:72px;top:488px;width:164px;height:54px">FREE ESTIMATE</a>
  <a class="btn btn-outline" style="left:258px;top:488px;width:164px;height:54px">LEARN MORE</a>
</section>

<section class="about">
  <div class="about-frame"></div>
  <div class="about-photo" role="img" aria-label="Freshly painted two-storey house with garden"></div>
  <h2>ABOUT US</h2>
  <div class="title-rule"></div>
  <p>Lorem ipsum dolor sit amet, consectetur adipiscing elit. Nulla volutpat neque at sapien quis pretium. Donec ultricies convallis sagittis. Vestibulum at dapibus justo. Fusce risus dolor, tincidunt in magna id, fermentum accumsan arcu. Proin sed lacinia elit ut erat nec ipsum mattis iaculis. Nam ac lobortis urna. Fusce gravida nunc ultrices nisi vehicula, tincidunt tortor laoreet. Aliquam in lacus fermentum, dapibus magna non, cursus neque. Ut at eros ac ante consectetur tristique. Nulla nisl nisi, mollis in nibh a, vehicula placerat urna. Pellentesque ultrices ante feu giat nisi volutpat, nec tempus dia volutpat. Sed vitae erat ullam corper, sollicitu din velit quis, viverra sapien.</p>
  <a class="btn btn-navy" style="left:556px;top:500px;width:150px;height:48px">KNOW MORE</a>
</section>

<section class="services">
  <div class="services-band" role="img" aria-label="Red-toned painted interior backdrop"></div>
  <h2 class="section-title">OUR SERVICES</h2>
  <div class="title-rule"></div>
  <p class="lead">Lorem ipsum dolor sit amet, consectetur adipiscing elit. Nulla volutpat neque at sapien quis pretium. Donec ultricies convallis sagittis. Vestibulum at dapibus justo. Fusce risus dolor, tincidunt in magna id, fermentum accumsan arcu. Proin sed lacinia elit ut erat nec ipsum. Nam ac lobortis urna. Fusce gravida nunc nisi viverra sapien.</p>
  <div class="service-cards">
    <div class="service-card"><div class="photo" role="img" aria-label="Living room with lavender painted walls" style="background:linear-gradient(160deg,#8c7fb8,#c9c2dc 60%,#5b4f86)"></div><h3>Interior Painting</h3></div>
    <div class="service-card"><div class="photo" role="img" aria-label="Modern house exterior with red facade" style="background:linear-gradient(160deg,#9bb6d3,#c0463e 55%,#6b2a26)"></div><h3>Exterior Painting</h3></div>
    <div class="service-card"><div class="photo" role="img" aria-label="Kitchen with painted cabinets" style="background:linear-gradient(160deg,#d8cfc2,#a9937a 55%,#5e4c3a)"></div><h3>Cabinet Painting</h3></div>
    <div class="service-card"><div class="photo" role="img" aria-label="Room with decorative wallpaper" style="background:linear-gradient(160deg,#3c4a33,#8a9a5e 55%,#2a3224)"></div><h3>Wallpaper Services</h3></div>
  </div>
  <a class="btn btn-red" style="left:500px;top:678px;width:200px;height:54px">VIEW ALL SERVICES</a>
</section>

<section class="why">
  <h2 class="section-title">WHY CHOOSE BRUSHWELL CRAFTS?</h2>
  <div class="title-rule"></div>
  <p class="lead">Lorem ipsum dolor sit amet, consectetur adipiscing elit. Nulla volutpat neque at sapien quis pretium. Donec ultricies convallis sagittis. Vestibulum at dapibus justo. Fusce risus dolor, tincidunt in magna id, fermentum a.</p>
  <div class="why-cards">
    <div class="why-card navy"><div class="icon"><svg width="24" height="24" viewBox="0 0 24 24" fill="none" stroke="#fff" stroke-width="2"><path d="M12 2l8 4v6c0 5-4 8-8 10-4-2-8-5-8-10V6z"/><path d="M8 12l3 3 5-6"/></svg></div><h4>Fully Licensed &amp; Insured</h4><p>Lorem ipsum dolor sit amet, consectetur</p></div>
    <div class="why-card red"><div class="icon"><svg width="24" height="24" viewBox="0 0 24 24" fill="none" stroke="#fff" stroke-width="2"><rect x="5" y="4" width="14" height="18" rx="2"/><path d="M9 4V2h6v2M8 11h8M8 15h6"/></svg></div><h4>Free In Home Estimate</h4><p>Lorem ipsum dolor sit amet, consectetur</p></div>
    <div class="why-card navy"><div class="icon"><svg width="24" height="24" viewBox="0 0 24 24" fill="none" stroke="#fff" stroke-width="2"><path d="M4 12h14M13 6l6 6-6 6"/></svg></div><h4>Free Color Consultation</h4><p>Lorem ipsum dolor sit amet, consectetur</p></div>
    <div class="why-card red"><div class="icon"><svg width="24" height="24" viewBox="0 0 24 24" fill="none" stroke="#fff" stroke-width="2"><circle cx="12" cy="12" r="9"/><path d="M12 7v5l3 2"/></svg></div><h4>We Show Up On Time</h4><p>Lorem ipsum dolor sit amet, consectetur</p></div>
  </div>
</section>

<section class="cta" role="img" aria-label="Modern house at dusk with navy overlay">
  <h2>Contact us today to get your<br>FREE estimate!</h2>
  <a class="btn btn-red">CONTACT US</a>
</section>

<section class="reviews">
  <h2 class="section-title">CLIENT REVIEWS</h2>
  <div class="title-rule"></div>
  <div class="arrow" style="left:136px;top:478px;background:#b8bcc4"><svg width="14" height="14" viewBox="0 0 14 14"><path d="M9 2L4 7l5 5" stroke="#fff" stroke-width="2" fill="none"/></svg></div>
  <div class="arrow" style="left:1020px;top:478px;background:var(--navy)"><svg width="14" height="14" viewBox="0 0 14 14"><path d="M5 2l5 5-5 5" stroke="#fff" stroke-width="2" fill="none"/></svg></div>

  <div class="review-box review-red"><span class="quote">“</span>Lorem ipsum dolor sit amet, con sectetur adipiscing elit. Vivamus nisi ex, luctus eu ipsum porta, viverra at amet est. Vivamus eu mauris convallis, hendrerit</div>
  <svg class="abs" style="left:300px;top:518px" width="30" height="20"><polygon points="0,0 30,0 6,20" fill="#b4173a"/></svg>
  <div class="avatar" role="img" aria-label="Client portrait" style="left:280px;top:552px"></div>
  <div class="reviewer abs" style="left:360px;top:560px"><h4>Owen Carter</h4><span>Lorem ipsum dolor</span><div class="stars">★★★★★</div></div>

  <div class="avatar" role="img" aria-label="Client portrait" style="left:664px;top:332px"></div>
  <div class="reviewer abs" style="left:744px;top:338px"><h4>Daniel Brooks</h4><span>Lorem ipsum dolor</span><div class="stars">★★★★★</div></div>
  <svg class="abs" style="left:690px;top:398px" width="30" height="20"><polygon points="6,0 30,20 0,20" fill="#0f2147"/></svg>
  <div class="review-box review-navy"><span class="quote">“</span>Lorem ipsum dolor sit amet, con sectetur adipiscing elit. Vivamus nisi ex, luctus eu ipsum porta, viverra at amet est. Vivamus eu mauris convallis, hendrerit</div>
</section>

<section class="gallery">
  <h2 class="section-title">OUR GALLERY</h2>
  <div class="title-rule"></div>
  <div class="arrow" style="left:72px;top:324px;background:#b8bcc4"><svg width="14" height="14" viewBox="0 0 14 14"><path d="M9 2L4 7l5 5" stroke="#fff" stroke-width="2" fill="none"/></svg></div>
  <div class="arrow" style="left:1084px;top:324px;background:var(--navy)"><svg width="14" height="14" viewBox="0 0 14 14"><path d="M5 2l5 5-5 5" stroke="#fff" stroke-width="2" fill="none"/></svg></div>
  <div class="gallery-row">
    <div role="img" aria-label="Bright white kitchen interior" style="background:linear-gradient(160deg,#f1ece4,#c9b89e 60%,#7a6a55)"></div>
    <div role="img" aria-label="Brick townhouse exterior" style="background:linear-gradient(160deg,#a9c4de,#a0674a 55%,#5c3b2a)"></div>
    <div role="img" aria-label="Living room with neutral walls" style="background:linear-gradient(160deg,#ece9e4,#b3aa9c 60%,#6f665a)"></div>
    <div role="img" aria-label="White gabled house with lawn" style="background:linear-gradient(160deg,#8fb6dc,#e9eef2 50%,#5f8a3c)"></div>
  </div>
</section>

<footer class="site-footer">
  <div class="brand"><span class="brand-mark"></span>Brushwell Crafts</div>
  <div class="socials"><span></span><span></span><span></span><span></span></div>
  <div class="foot-col" style="left:384px">
    <h4>Quick Links</h4>
    <ul><li>About Us</li><li>Services</li><li>Testimonials</li><li>Gallery</li><li>Contact Us</li></ul>
  </div>
  <div class="foot-col" style="left:576px">
    <h4>Contact Us</h4>
    <div class="contact-item"><span class="ic"></span><div>CALL US<br>(209) 555-0148</div></div>
    <div class="contact-item"><span class="ic"></span><div>EMAIL US<br>info@brushwellcrafts.com</div></div>
    <div class="contact-item"><span class="ic"></span><div>Address line dummy here<br>Address line dummy</div></div>
  </div>
  <div class="foot-col newsletter" style="left:876px">
    <h4>Our Newsletter</h4>
    <p>Subscribe our newsletter to get the latest news.</p>
    <div class="field"></div>
    <a class="btn btn-red">SUBSCRIBE</a>
  </div>
</footer>
<div class="copyright">Copyright © 2024 All Rights Reserved by Brushwell Crafts</div>

</body>
</html>
```